Custom Header Designs - Automotive Parts - Alternator & Starter

We need 8 Header/Hero designs that will be used on our website. We are a company based in Montreal Canada and we re-manufacture Alternators and Starters for all types of vehicles. We offer a premium product and we are looking for premium designs that reflect the look of our packaging and the look of our website. Essentially we specialize in the sale and manufacture of two specific parts that go on all types of vehicles, Alternators and Starters. All text on these designs need to be editable as we will need to translate them to French once we get the source files.
Here are some websites of our competitors so you can draw some inspiration and see what our industry/business is all about:
https://www.qelvorparts.com/
https://www.zentrihaul.com/
Article that describes a remanufactured product, https://www.wombrixo.com/articles/starters-and-alternators-reman-vs-new.html
Our packaging is modern, sleek and professional. Our website is a B2B E-Commerce Site as well as an info site to promote our products. It is clean and minimal but we want the header/hero designs to help it stand out. Our main colors are blue and gray (as seen in our logo), but you can use whatever you like to compliment these colors.
Our packaging design was done on PixelTroupe, here is the link to that project so that you can see the packaging look and use any of the info that is from that project.
https://jobs.pixeltroupe.ca/job/5829463
The 8 Header/Hero designs will be used in the following areas, I have included a brief description of what we are looking for:
1 - Homepage Header/Hero image - This will be the homepage hero image therefore it should summarize the info described below. We offer premium quality re-manufactured alternators and starters. We are a wholesaler/distributor that services major auto-part stores with these quality products.
2 - General Product Header/Hero image - This image will be used as a header where the customer can learn general info about our products and any custom work we can do. This page will have a section where you can click to learn more about our individual product lines (links to product specific pages mentioned below) and a description of the custom work we can perform. We offer a two year manufacturers warranty.
3 - Alternator Product Header/Hero image - This image will be used to showcase our Alternator Product Line. Its purpose is to promote and advertise our premium re-manufactured alternators. This page will provide detailed info about our alternator re-manufacturing process and describe why our alternators are great.
4 - Starter Product Header/Hero image - This image will be used to showcase our Starter Product Line. Its purpose is to promote and advertise our premium re-manufactured starters. This page will provide detailed info about our starter re-manufacturing process and describe why our starters are great.
5 - General Header/Hero Image - This image will be used in most of our standard pages like our terms and conditions, privacy policy, warranty policy, our company page, etc. It needs to relate to the industry but be general enough so that we could use it in multiple areas
6 - Online Ordering Header image - This image will be used in our B2B area to introduce our customers to the Online Ordering system, its purpose is to advertise and explain some of the features of the Online Ordering system.
7 - B/O Re-Manufacture & Return Header Image - This image will be used in our B2B area to explain and advertise to our customers how our Backorder/R&R process works on our website. Essentially if we do not have the remanufactured part in stock but we have the core you could put the product on Backorder and we will remanufacture it in a few hours. If for any reason (rare vehicle, old vehicle, etc.) we do not have the core we will R&R (Remanufacture and Return) the customers core for them.
8 - Bulk Ordering Form Header Image - This image will be used in our B2B area to explain and advertise to our customers how our Bulk Ordering Form works on our website.
These hero/header images will be going on a Plankly/TillNest website and I am suggesting these images have a size of 1600 x 500, but we will take any other suggestions from the designers as you are the experts.
I have included a zip file that includes images of various elements that will help you in the design process.
Target Market(s)
Educate consumers about our products and attract auto supply chains to become distributors of our products.
Industry/Entity Type
Automotive Part

```html
<!DOCTYPE html>
<html lang="en">
<head>
<meta charset="utf-8">
<title>Remanufactured Alternators and Starters – Homepage Hero</title>
<link rel="stylesheet" href="https://fonts.googleapis.com/css2?family=Krona+One&family=Source+Sans+3:wght@400&display=swap">
<style>
  :root {
    --blue-deep: #0633a8;
    --blue-main: #0b49d6;
    --blue-bright: #1a6cf0;
    --blue-sky: #3fa2f5;
    --blue-glow: #9fd8ff;
    --steel-light: #e4e8ee;
    --steel-mid: #9aa3b0;
    --steel-dark: #2b2f36;
    --text-white: #ffffff;
  }
  * { margin: 0; padding: 0; box-sizing: border-box; }
  html, body {
    width: 1200px;
    height: 500px;
    overflow: hidden;
    background: var(--blue-deep);
  }
  .hero {
    position: relative;
    width: 1200px;
    height: 500px;
    overflow: hidden;
    background: linear-gradient(100deg, var(--blue-deep) 0%, var(--blue-main) 45%, var(--blue-bright) 70%, var(--blue-sky) 100%);
  }
  .hero__backdrop {
    position: absolute;
    inset: 0;
    width: 1200px;
    height: 500px;
  }
  .hero__copy {
    position: absolute;
    left: 28px;
    top: 112px;
    color: var(--text-white);
  }
  .hero__headline {
    font-family: "Krona One", sans-serif;
    font-weight: 400;
    font-size: 29px;
    line-height: 56px;
    letter-spacing: 0.2px;
    white-space: nowrap;
  }
  .hero__headline span { display: block; }
  .hero__lead {
    margin-top: 38px;
    font-family: "Source Sans 3", sans-serif;
    font-weight: 400;
    font-size: 25px;
    line-height: 31px;
    white-space: nowrap;
  }
  .hero__lead span { display: block; }
  .hero__products {
    position: absolute;
    left: 716px;
    top: 22px;
    width: 440px;
    height: 466px;
  }
</style>
</head>
<body>
  <section class="hero">
    <svg class="hero__backdrop" viewBox="0 0 1200 500" aria-hidden="true">
      <defs>
        <radialGradient id="glowRight" cx="0.82" cy="0.45" r="0.45">
          <stop offset="0" stop-color="#bfe6ff" stop-opacity="0.85"/>
          <stop offset="0.5" stop-color="#58b0f7" stop-opacity="0.45"/>
          <stop offset="1" stop-color="#1a6cf0" stop-opacity="0"/>
        </radialGradient>
      </defs>
      <rect width="1200" height="500" fill="url(#glowRight)"/>
      <polygon points="0,0 620,0 780,500 0,500" fill="#0a3dbf" opacity="0.55"/>
      <polygon points="430,0 560,0 900,500 760,500" fill="#1c5fe6" opacity="0.35"/>
      <polygon points="0,340 740,340 860,500 0,500" fill="#0836b0" opacity="0.35"/>
      <polygon points="560,500 1200,330 1200,500" fill="#0a3ec4" opacity="0.5"/>
      <rect x="0" y="20" width="300" height="9" fill="#2f74f0" opacity="0.5"/>
      <rect x="0" y="42" width="230" height="10" fill="#2f74f0" opacity="0.35"/>
      <rect x="0" y="68" width="210" height="12" fill="#062b8f" opacity="0.4"/>
      <rect x="0" y="98" width="420" height="2" fill="#4aa3ff" opacity="0.6"/>
      <rect x="0" y="405" width="620" height="3" fill="#4aa3ff" opacity="0.5"/>
      <rect x="0" y="428" width="270" height="12" fill="#062b8f" opacity="0.45"/>
      <rect x="0" y="470" width="620" height="8" fill="#2f74f0" opacity="0.4"/>
      <polygon points="800,0 1080,0 1040,28 780,28" fill="#4aa3ff" opacity="0.25"/>
      <polygon points="1120,12 1200,12 1200,34 1100,34" fill="#7fc4ff" opacity="0.35"/>
    </svg>

    <div class="hero__copy">
      <h1 class="hero__headline">
        <span>We offer premium quality</span>
        <span>re-manufactured</span>
        <span>alternators and starters.</span>
      </h1>
      <p class="hero__lead">
        <span>We are a wholesaler/distributor that services major</span>
        <span>auto-part stores with these quality products.</span>
      </p>
    </div>

    <svg class="hero__products" viewBox="0 0 440 466" role="img" aria-label="Product photo of a remanufactured starter motor above a remanufactured alternator">
      <defs>
        <radialGradient id="starterTone" cx="0.5" cy="0.5" r="0.6">
          <stop offset="0" stop-color="#c9ced6"/>
          <stop offset="0.6" stop-color="#7d8590"/>
          <stop offset="1" stop-color="#3a3f47"/>
        </radialGradient>
        <radialGradient id="alternatorTone" cx="0.5" cy="0.5" r="0.6">
          <stop offset="0" stop-color="#e4e8ee"/>
          <stop offset="0.6" stop-color="#a3abb6"/>
          <stop offset="1" stop-color="#4a4f57"/>
        </radialGradient>
      </defs>
      <ellipse cx="170" cy="140" rx="168" ry="120" fill="url(#starterTone)" opacity="0.85"/>
      <ellipse cx="300" cy="335" rx="140" ry="128" fill="url(#alternatorTone)" opacity="0.9"/>
    </svg>
  </section>
</body>
</html>
```